VornaDerm/The experts in permanent hairremoval

Our Brand is VornaDerm and we are specialized on permantent hair removal for the body for men and woman. VornaDerm is working as a Franchise chain.
The brand should be positioned as lifestyle brand but with a medical background. People should trust in us. We take care about their body. This need to be communicated 100%.
Our system is inexpensive but we don't want to show that we are cheap. So we want to communicate that permanent hair removal is a real lifestyle product but affordable.
We already created a logo that you can see the style and colour we prefer.

Target Market(s)

Europe beginning (especially german spoken markets), Middle East, Africa

Industry/Entity Type

Hair Removal

Number of Pages Required

5+ page

Font styles to use
Serif
Other font styles liked:
• Trajan Pro

Requirements
Nice to have
• We are very open for new ideas

```html
<!DOCTYPE html>
<html lang="en">
<head>
<meta charset="utf-8">
<title>VornaDerm – The Experts in Permanent Hair Removal</title>
<link href="https://fonts.googleapis.com/css2?family=Cinzel:wght@400;600&family=Roboto:wght@400;500;700&family=Roboto+Condensed:wght@400;700&display=swap" rel="stylesheet">
<style>
:root{
  --blue:#3d9fdc;
  --blue-dark:#2a88c8;
  --blue-nav:#4aa8e0;
  --blue-band:#3a9ad8;
  --ink:#333333;
  --ink-soft:#666666;
  --grey-nav:#7a7a7a;
  --footer:#2e2e2e;
  --footer-base:#222222;
  --white:#ffffff;
}
*{box-sizing:border-box;margin:0;padding:0}
html,body{width:1200px;height:3000px;overflow:hidden;background:var(--white)}
body{position:relative;font-family:"Roboto",Arial,sans-serif;color:var(--ink)}
.abs{position:absolute}
.serif{font-family:"Cinzel","Times New Roman",serif}
.cond{font-family:"Roboto Condensed","Arial Narrow",sans-serif}

/* top bar */
.topbar{top:0;left:0;width:1200px;height:44px;border-bottom:1px solid #e6e6e6}
.social{left:90px;top:14px;display:flex;gap:20px}
.social span{width:16px;height:16px;border-radius:50%;background:var(--blue)}
.consult{right:76px;top:8px;display:flex;align-items:center;gap:12px;font-size:19px}
.consult .phone-ring{width:34px;height:34px;border:2px solid var(--blue);border-radius:50%;display:flex;align-items:center;justify-content:center}
.consult strong{color:var(--blue);font-weight:700;font-family:"Roboto Condensed",sans-serif;font-size:21px;margin-left:6px}

/* header */
.brand{left:76px;top:62px;display:flex;align-items:center;gap:14px}
.brand-dot{width:56px;height:56px;border-radius:50%;background:var(--blue)}
.brand-name{font-family:"Roboto",Arial,sans-serif;font-size:52px;font-weight:400;color:#555555;line-height:1}
.brand-tag{left:150px;top:124px;font-size:10px;letter-spacing:1px;color:#777;text-transform:uppercase}
.btn-book{left:842px;top:78px;width:280px;height:52px;background:var(--blue);color:#fff;display:flex;align-items:center;font-family:"Roboto Condensed",sans-serif;font-weight:700;font-size:20px;letter-spacing:.5px}
.btn-book span{flex:1;text-align:center}
.btn-book i{width:50px;height:52px;background:var(--blue-dark);display:flex;align-items:center;justify-content:center}

/* nav */
.nav{top:170px;left:0;width:1200px;height:56px;background:var(--blue-nav);display:flex;padding-left:76px}
.nav a{color:#fff;text-decoration:none;font-family:"Roboto Condensed",sans-serif;font-size:19px;display:flex;align-items:center;padding:0 32px;height:56px;position:relative}
.nav a+a::before{content:"";position:absolute;left:0;top:14px;height:28px;border-left:1px solid rgba(255,255,255,.55)}
.nav a.active{background:var(--grey-nav);padding:0 34px}
.nav a.active+a::before{display:none}

/* hero */
.hero{top:226px;left:0;width:1200px;height:468px;background:linear-gradient(90deg,#c4c4c4 0%,#dadada 45%,#ececec 100%)}
.hero-photo{left:560px;top:0;width:640px;height:468px;background:radial-gradient(ellipse at 60% 45%,#f2e0d2 0%,#e6d2c4 35%,rgba(236,236,236,0) 70%)}
.hero h1{left:80px;top:96px;font-family:"Cinzel",serif;font-weight:400;font-size:50px;line-height:68px;color:var(--blue-dark)}
.hero p{left:80px;top:232px;font-size:25px;color:#444}
.btn-outline{border:2px solid #555;color:#333;font-family:"Roboto Condensed",sans-serif;font-weight:700;display:flex;align-items:center;justify-content:center;border-radius:3px}
.hero .btn-outline{left:76px;top:290px;width:254px;height:52px;font-size:23px}

/* welcome */
.welcome{top:694px;left:0;width:1200px;height:308px}
.welcome h2{top:40px;left:0;width:1200px;text-align:center;font-size:50px;font-weight:400;color:#333}
.welcome h2 em{font-style:normal;color:var(--blue)}
.welcome p{top:114px;left:180px;width:840px;text-align:center;font-size:16px;line-height:26px;color:var(--ink-soft)}
.welcome .btn-outline{left:442px;top:198px;width:316px;height:52px;font-size:23px;border-color:#888;color:#555}
.welcome-photo{left:960px;top:12px;width:240px;height:296px;background:radial-gradient(ellipse at 50% 55%,#d9b79e 0%,#e9d3c4 45%,rgba(255,255,255,0) 72%)}

/* why */
.why{top:1002px;left:0;width:1200px;height:470px;background:radial-gradient(ellipse at 20% 40%,#8fcaf0 0%,#5ab0e6 40%,#4aa6e2 100%)}
.why-photo{left:60px;top:20px;width:260px;height:450px;background:linear-gradient(180deg,rgba(255,255,255,.25) 0%,#e8c3a8 55%,#d8a88c 100%);border-radius:120px 120px 0 0}
.why h2{top:34px;left:300px;width:770px;text-align:center;font-size:44px;font-weight:400;color:#fff}
.feature{top:126px;width:240px;text-align:center;color:#fff}
.feature .circle{width:144px;height:144px;border-radius:50%;background:var(--blue-dark);margin:0 auto;display:flex;align-items:center;justify-content:center}
.feature h3{font-family:"Cinzel",serif;font-weight:400;font-size:28px;margin-top:24px}
.feature p{font-size:16px;line-height:25px;margin-top:10px;padding:0 16px}

/* procedures band */
.band{top:1472px;left:0;width:1200px;height:154px;background:var(--blue-band)}
.band p{left:80px;top:36px;font-family:"Cinzel",serif;font-size:30px;line-height:46px;color:#fff}
.btn-white{left:864px;top:56px;width:256px;height:56px;border:2px solid rgba(255,255,255,.85);border-radius:3px;color:#fff;font-family:"Roboto Condensed",sans-serif;font-size:26px;display:flex;align-items:center;justify-content:center;gap:14px}

/* team */
.team{top:1626px;left:0;width:1200px;height:384px}
.section-title{left:0;width:1200px;text-align:center;font-family:"Cinzel",serif;font-weight:400;font-size:48px;color:#333}
.section-title em{font-style:normal;color:var(--blue)}
.team .section-title{top:34px}
.member-photo{width:210px;height:210px;border:2px solid var(--blue);border-radius:6px;background:linear-gradient(180deg,#dbe8f2 0%,#cfdfec 55%,#5f7fa6 100%);top:104px}
.member{top:112px;width:264px}
.member h4{font-family:"Roboto Condensed",sans-serif;font-weight:400;font-size:22px;color:var(--blue)}
.member h5{font-weight:400;font-size:17px;color:#222;margin-top:8px}
.member p{font-size:15px;line-height:25px;color:#666;margin-top:10px}
.team-divider{left:600px;top:134px;width:2px;height:212px;background:#9a9a9a}

/* testimonials */
.testimonials{top:2010px;left:0;width:1200px;height:372px;background:linear-gradient(180deg,#e4e6e8 0%,#eef0f1 50%,#e2e4e5 100%)}
.testimonials .section-title{top:36px}
.video{left:76px;top:130px;width:362px;height:196px;border:2px solid var(--blue);background:linear-gradient(90deg,#6b6256 0%,#b89c86 45%,#7c6d60 100%)}
.play{left:158px;top:76px;width:44px;height:44px;border-radius:50%;background:rgba(255,255,255,.9);display:flex;align-items:center;justify-content:center}
.quote-mark{left:478px;top:138px;font-family:"Cinzel",serif;font-size:80px;line-height:1;color:var(--blue);font-weight:600}
.quote{left:476px;top:196px;width:560px;font-size:16px;line-height:25px;color:#333}
.client{left:476px;top:298px;font-size:15px;color:var(--blue)}
.dots{left:476px;top:328px;display:flex;gap:14px}
.dots span{width:16px;height:16px;border-radius:50%;background:#8a8a8a}
.dots span.on{background:var(--blue)}

/* news */
.news{top:2382px;left:0;width:1200px;height:346px}
.news .section-title{top:44px}
.post{top:128px;width:330px;display:flex;gap:16px}
.date{width:60px;flex:none}
.date .day{height:48px;background:var(--blue);color:#fff;font-size:32px;font-weight:500;display:flex;align-items:center;justify-content:center}
.date .mon{height:40px;background:#e3e3e3;color:#444;font-size:18px;display:flex;align-items:center;justify-content:center}
.post h4{font-size:14px;line-height:21px;color:var(--blue);font-weight:700}
.post p{font-size:14px;line-height:20px;color:#555;margin-top:4px}
.post a{display:inline-block;margin-top:6px;font-size:13px;font-weight:700;color:var(--blue);text-decoration:underline}

/* footer */
.footer{top:2728px;left:0;width:1200px;height:230px;background:var(--footer);color:#fff}
.footer h4{font-family:"Cinzel",serif;font-weight:400;font-size:28px;color:var(--blue);top:32px}
.links{top:84px;font-size:16px;line-height:25px}
.links .current{color:var(--blue)}
.hours{top:84px;left:446px;font-size:16px;line-height:32px}
.hours b{display:inline-block;width:178px;font-weight:700}
.contact{top:80px;left:812px;font-size:16px;line-height:32px}
.contact div{display:flex;align-items:center;gap:10px}
.copyright{top:2958px;left:0;width:1200px;height:42px;background:var(--footer-base);color:#cfcfcf;font-size:15px;display:flex;align-items:center;justify-content:center}
.copyright b{color:var(--blue);margin-right:4px}
</style>
</head>
<body>

<!-- top bar -->
<div class="abs topbar">
  <div class="abs social"><span></span><span></span><span></span></div>
  <div class="abs consult">Request a consultation
    <span class="phone-ring"><svg width="18" height="18" viewBox="0 0 24 24"><path fill="#3d9fdc" d="M6.6 10.8c1.4 2.8 3.8 5.1 6.6 6.6l2.2-2.2c.3-.3.7-.4 1-.2 1.1.4 2.3.6 3.6.6.6 0 1 .4 1 1V20c0 .6-.4 1-1 1C10.6 21 3 13.4 3 4c0-.6.4-1 1-1h3.5c.6 0 1 .4 1 1 0 1.3.2 2.5.6 3.6.1.3 0 .7-.2 1l-2.3 2.2z"/></svg></span>
    <strong>01 555 0192</strong>
  </div>
</div>

<!-- header -->
<div class="abs brand"><span class="brand-dot"></span><span class="brand-name">VornaDerm</span></div>
<div class="abs brand-tag">The experts in permanent hair removal</div>
<div class="abs btn-book"><span>BOOK APPOINTMENT</span><i><svg width="16" height="22" viewBox="0 0 16 22"><path d="M3 2l9 9-9 9" stroke="#fff" stroke-width="4" fill="none"/></svg></i></div>

<nav class="abs nav">
  <a class="active">HOME</a><a>ABOUT</a><a>STUDIOS</a><a>BOOK APPOINTMENT</a><a>JOB</a><a>FRANCHISE</a><a>CONTACT</a>
</nav>

<!-- hero -->
<section class="abs hero">
  <div class="abs hero-photo" role="img" aria-label="Photo of a woman in a white towel sitting with smooth bare legs"></div>
  <h1 class="abs">Are you Ready to<br>Smooth Hair Free Skin?</h1>
  <p class="abs">Lorem Ipsum is simply dummy text of the printing.</p>
  <div class="abs btn-outline">CONTACT US NOW!</div>
</section>

<!-- welcome -->
<section class="abs welcome">
  <h2 class="abs serif">Welcome to <em>Vorna Derm</em></h2>
  <p class="abs">Lorem Ipsum is simply dummy text of the printing and typesetting industry. Lorem Ipsum has been the industry's standard dummy text ever since the 1500s.</p>
  <div class="abs btn-outline">BOOK AN APPOINTMENT</div>
  <div class="abs welcome-photo" role="img" aria-label="Photo of a shirtless man touching his neck"></div>
</section>

<!-- why -->
<section class="abs why">
  <div class="abs why-photo" role="img" aria-label="Photo of a raised hand pointing up"></div>
  <h2 class="abs serif">Why Permanent Epilation</h2>
  <div class="abs feature" style="left:376px">
    <div class="circle"><svg width="64" height="64" viewBox="0 0 64 64" fill="none" stroke="#fff" stroke-width="3"><path d="M32 14a13 13 0 0 0-8 23c2 2 3 4 3 6h10c0-2 1-4 3-6a13 13 0 0 0-8-23z"/><path d="M27 48h10M28 53h8"/><path d="M32 4v5M14 12l3 3M50 12l-3 3M8 28h5M56 28h-5" stroke-linecap="round"/></svg></div>
    <h3>The Method</h3>
    <p>Lorem Ipsum is simply dummy text of the printing and typesetting industry.</p>
  </div>
  <div class="abs feature" style="left:628px">
    <div class="circle"><svg width="64" height="64" viewBox="0 0 64 64"><path fill="#fff" d="M10 28h10v26H10zM24 52V30l10-16c2-3 6-1 5 2l-3 10h14c3 0 5 3 4 6l-5 16c-1 3-3 4-5 4z"/></svg></div>
    <h3>Good to Know</h3>
    <p>Lorem Ipsum is simply dummy text of the printing and typesetting industry.</p>
  </div>
  <div class="abs feature" style="left:890px">
    <div class="circle"><svg width="64" height="64" viewBox="0 0 64 64" fill="#fff"><rect x="25" y="8" width="14" height="12"/><rect x="8" y="42" width="14" height="12"/><rect x="25" y="42" width="14" height="12"/><rect x="42" y="42" width="14" height="12"/><path d="M31 20h2v10h17v12h-2V32H33v10h-2V32H16v10h-2V30h17z"/></svg></div>
    <h3>Zones</h3>
    <p>Lorem Ipsum is simply dummy text of the printing and typesetting industry.</p>
  </div>
</section>

<!-- procedures -->
<section class="abs band">
  <p class="abs">We provide a complete range of surgical &amp;<br>non-surgical hair removal procedures</p>
  <div class="abs btn-white">All Procedures <svg width="14" height="22" viewBox="0 0 14 22"><path d="M2 2l9 9-9 9" stroke="#fff" stroke-width="4" fill="none"/></svg></div>
</section>

<!-- team -->
<section class="abs team">
  <h2 class="abs section-title">Our <em>Team</em></h2>
  <div class="abs member-photo" style="left:76px" role="img" aria-label="Portrait photo of a smiling doctor in a white coat"></div>
  <div class="abs member" style="left:304px">
    <h4>Dr Vorna Derm Doctor Name</h4>
    <h5>Principal Expert and Owner</h5>
    <p>Lorem Ipsum is simply dummy text of the printing and typesetting industry. Lorem Ipsum has been the industry's standard dummy text ever since the 1500s.</p>
  </div>
  <div class="abs team-divider"></div>
  <div class="abs member-photo" style="left:636px" role="img" aria-label="Portrait photo of a smiling doctor in shirt and tie"></div>
  <div class="abs member" style="left:864px">
    <h4>Dr Vorna Derm Doctor Name</h4>
    <h5>Principal Expert and Co-Owner</h5>
    <p>Lorem Ipsum is simply dummy text of the printing and typesetting industry. Lorem Ipsum has been the industry's standard dummy text ever since the 1500s.</p>
  </div>
</section>

<!-- testimonials -->
<section class="abs testimonials" role="img" aria-label="Faded photo of a bright treatment room behind the client quotes">
  <h2 class="abs section-title">What Our <em>Client Say</em></h2>
  <div class="abs video" role="img" aria-label="Video still of a smiling client">
    <div class="abs play"><svg width="18" height="20" viewBox="0 0 18 20"><path d="M2 1l15 9-15 9z" fill="#3d9fdc"/></svg></div>
  </div>
  <div class="abs quote-mark">“</div>
  <p class="abs quote">Lorem Ipsum is simply dummy text of the printing and typesetting industry. Lorem Ipsum has been the industry's standard dummy text ever since the 1500s.</p>
  <div class="abs client">- Client Name</div>
  <div class="abs dots"><span class="on"></span><span></span><span></span><span></span></div>
</section>

<!-- news -->
<section class="abs news">
  <h2 class="abs section-title">Vorna Derm <em>News</em></h2>
  <article class="abs post" style="left:76px">
    <div class="date"><div class="day">17</div><div class="mon">Nov</div></div>
    <div><h4>Lorem Ipsum is simply dummy text of the printi</h4><p>Lorem Ipsum is simply dummy text of the printing and typesetting industry...</p><a>READ MORE</a></div>
  </article>
  <article class="abs post" style="left:442px">
    <div class="date"><div class="day">16</div><div class="mon">Nov</div></div>
    <div><h4>Lorem Ipsum is simply dummy text of the printi</h4><p>Lorem Ipsum is simply dummy text of the printing and typesetting industry....</p><a>READ MORE</a></div>
  </article>
  <article class="abs post" style="left:808px">
    <div class="date"><div class="day">15</div><div class="mon">Nov</div></div>
    <div><h4>Lorem Ipsum is simply dummy text of the printi</h4><p>Lorem Ipsum is simply dummy text of the printing and typesetting industry....</p><a>READ MORE</a></div>
  </article>
</section>

<!-- footer -->
<footer class="abs footer">
  <h4 class="abs" style="left:80px">Useful Links</h4>
  <div class="abs links" style="left:80px"><div class="current">Home</div><div>About</div><div>Studios</div><div>Book Appointment</div></div>
  <div class="abs links" style="left:256px"><div>Job</div><div>Franchise</div><div>Contact</div></div>
  <h4 class="abs" style="left:446px">Office Hours</h4>
  <div class="abs hours">
    <div><b>Monday to Friday :</b>8am to 7pm</div>
    <div><b>Saturday :</b>9am to 2pm</div>
    <div><b>Sunday</b>Closed</div>
  </div>
  <h4 class="abs" style="left:812px">Contact Info</h4>
  <div class="abs contact">
    <div><svg width="16" height="20" viewBox="0 0 16 20"><path fill="#3d9fdc" d="M8 0a7 7 0 0 0-7 7c0 5 7 13 7 13s7-8 7-13a7 7 0 0 0-7-7zm0 10a3 3 0 1 1 0-6 3 3 0 0 1 0 6z"/></svg>Lorem Ipsum is simply dummy text.</div>
    <div><svg width="18" height="18" viewBox="0 0 24 24"><path fill="#3d9fdc" d="M6.6 10.8c1.4 2.8 3.8 5.1 6.6 6.6l2.2-2.2c.3-.3.7-.4 1-.2 1.1.4 2.3.6 3.6.6.6 0 1 .4 1 1V20c0 .6-.4 1-1 1C10.6 21 3 13.4 3 4c0-.6.4-1 1-1h3.5c.6 0 1 .4 1 1 0 1.3.2 2.5.6 3.6.1.3 0 .7-.2 1l-2.3 2.2z"/></svg>123 456 7890</div>
    <div><svg width="18" height="18" viewBox="0 0 18 18"><rect x="1" y="5" width="16" height="12" rx="2" fill="#3d9fdc"/><rect x="4" y="1" width="10" height="6" fill="none" stroke="#3d9fdc" stroke-width="2"/></svg>123 456 7890</div>
    <div><svg width="18" height="14" viewBox="0 0 18 14"><rect x="1" y="1" width="16" height="12" fill="none" stroke="#3d9fdc" stroke-width="2"/><path d="M1 1l8 7 8-7" fill="none" stroke="#3d9fdc" stroke-width="2"/></svg>info@vornaderm.com</div>
  </div>
</footer>
<div class="abs copyright">©&nbsp;<b>Vorna Derm</b> - 2015. All Rights Reserved.</div>

</body>
</html>
```